Political themed graphic for contemporary church sermon series

Contemporary church in California need a graphic design for a sermon series. The sermon series will be focused on the upcoming presidential election. The sermon series is titled for the question "who will be the next president":

Title: 45
Subtitle: Who will it be / Does it matter

The design should use red, white and blue and should possibly have the amber lodge in the graphic somewhere. Maybe like a watermark or something to that effect.

Target Market(s)

Contemporary design,

Industry/Entity Type

Church

Font styles to use
Serif
Sans Serif

Colors
0555a3
ec1f27
ffffff

Requirements
Must have
• Political theme, red, white and blue (contemporary color palette). Amber lodge screened back in the design somewhere.
• the title large: 45
• and subtitle: Who will it be | Does it matter
Should not have
• I'm not looking for cheesy graphics with elephant and a donkey.

```html
<!DOCTYPE html>
<html lang="en">
<head>
<meta charset="utf-8">
<title>45 — Sermon Series</title>
<link rel="stylesheet" href="https://fonts.googleapis.com/css2?family=Josefin+Sans:wght@400&family=Libre+Baskerville:wght@700&display=swap">
<style>
  :root {
    --backdrop: #ececec;
    --navy-blue: #0555a3;
    --navy-light: #2c6fb4;
    --flag-red: #ec1f27;
    --title-red: #e8333c;
    --ribbon-red: #e42a31;
    --ribbon-shade: #a8161c;
    --deep-blue: #1d3f78;
    --white: #ffffff;
  }
  html, body {
    margin: 0;
    padding: 0;
    width: 960px;
    height: 1200px;
    overflow: hidden;
    background: var(--backdrop);
  }
  .poster {
    position: absolute;
    left: 28px;
    top: 0;
    width: 904px;
    height: 1200px;
    background: var(--white);
    overflow: hidden;
  }
  .stripes {
    position: absolute;
    left: 0;
    width: 100%;
  }
  .stripes--top { top: 0; height: 141px; }
  .stripes--bottom { top: 1062px; height: 138px; }
  .field {
    position: absolute;
    left: 0;
    top: 141px;
    width: 100%;
    height: 921px;
    background: linear-gradient(180deg, var(--navy-light) 0%, var(--navy-blue) 60%, #0a4f99 100%);
  }
  .star-row {
    position: absolute;
    left: 0;
    width: 100%;
    height: 40px;
  }
  .star-row--top { top: 155px; }
  .star-row--bottom { top: 999px; }
  .landmark {
    position: absolute;
    left: 0;
    top: 220px;
    width: 904px;
    height: 780px;
    background: radial-gradient(ellipse 45% 60% at 50% 55%, rgba(120, 170, 225, 0.18), rgba(120, 170, 225, 0) 100%);
  }
  .series-title {
    position: absolute;
    left: 0;
    top: 220px;
    width: 100%;
    margin: 0;
    text-align: center;
    font-family: "Josefin Sans", sans-serif;
    font-weight: 400;
    font-size: 560px;
    line-height: 560px;
    letter-spacing: -40px;
    color: var(--title-red);
    text-shadow: -10px 8px 0 var(--deep-blue);
  }
  .ribbon {
    position: absolute;
    left: 0;
    top: 800px;
    width: 904px;
    height: 110px;
  }
  .subtitle {
    position: absolute;
    top: 838px;
    margin: 0;
    font-family: "Libre Baskerville", serif;
    font-weight: 700;
    font-size: 40px;
    line-height: 48px;
    white-space: nowrap;
  }
  .subtitle--question {
    left: 105px;
    color: var(--deep-blue);
    text-shadow: 2px 2px 0 rgba(255, 255, 255, 0.35);
  }
  .subtitle--answer {
    left: 470px;
    color: var(--white);
  }
</style>
</head>
<body>
  <main class="poster">
    <svg class="stripes stripes--top" viewBox="0 0 904 141" preserveAspectRatio="none" aria-hidden="true">
      <rect x="0" y="0" width="904" height="16" fill="var(--flag-red)"/>
      <rect x="0" y="48" width="904" height="32" fill="var(--flag-red)"/>
      <rect x="0" y="112" width="904" height="29" fill="var(--flag-red)"/>
    </svg>

    <div class="field"></div>

    <div class="landmark" role="img" aria-label="Faint screened-back Amber lodge building with dome"></div>

    <svg class="star-row star-row--top" viewBox="0 0 904 40" aria-hidden="true">
      <defs>
        <polygon id="star" points="0,-15 3.5,-4.6 14.3,-4.6 5.6,1.8 8.8,12.1 0,5.7 -8.8,12.1 -5.6,1.8 -14.3,-4.6 -3.5,-4.6" fill="var(--white)"/>
      </defs>
      <use href="#star" x="46" y="20"/><use href="#star" x="105" y="20"/><use href="#star" x="164" y="20"/>
      <use href="#star" x="223" y="20"/><use href="#star" x="282" y="20"/><use href="#star" x="341" y="20"/>
      <use href="#star" x="400" y="20"/><use href="#star" x="459" y="20"/><use href="#star" x="518" y="20"/>
      <use href="#star" x="577" y="20"/><use href="#star" x="636" y="20"/><use href="#star" x="695" y="20"/>
      <use href="#star" x="754" y="20"/><use href="#star" x="813" y="20"/><use href="#star" x="872" y="20"/>
    </svg>

    <h1 class="series-title">45</h1>

    <svg class="ribbon" viewBox="0 0 904 110" aria-hidden="true">
      <polygon points="75,22 125,22 125,102 75,102 96,62" fill="var(--ribbon-shade)"/>
      <polygon points="829,22 779,22 779,102 829,102 808,62" fill="var(--ribbon-shade)"/>
      <rect x="105" y="10" width="694" height="84" fill="var(--ribbon-red)"/>
    </svg>
    <p class="subtitle subtitle--question">Who will it be</p>
    <p class="subtitle subtitle--answer">Does it matter</p>

    <svg class="star-row star-row--bottom" viewBox="0 0 904 40" aria-hidden="true">
      <use href="#star" x="46" y="20"/><use href="#star" x="105" y="20"/><use href="#star" x="164" y="20"/>
      <use href="#star" x="223" y="20"/><use href="#star" x="282" y="20"/><use href="#star" x="341" y="20"/>
      <use href="#star" x="400" y="20"/><use href="#star" x="459" y="20"/><use href="#star" x="518" y="20"/>
      <use href="#star" x="577" y="20"/><use href="#star" x="636" y="20"/><use href="#star" x="695" y="20"/>
      <use href="#star" x="754" y="20"/><use href="#star" x="813" y="20"/><use href="#star" x="872" y="20"/>
    </svg>

    <svg class="stripes stripes--bottom" viewBox="0 0 904 138" preserveAspectRatio="none" aria-hidden="true">
      <rect x="0" y="29" width="904" height="32" fill="var(--flag-red)"/>
      <rect x="0" y="93" width="904" height="30" fill="var(--flag-red)"/>
    </svg>
  </main>
</body>
</html>
```